Price list for young Relaxon clinic

I require a price list/Treatment menu for clinic

To include:
Logo
Address
Phone number
Website

List of services and Prices
Relaxon 1 area £100
Relaxon 2 areas £150
Relaxon 3 areas £200
Lip Enhancement 0.5ml £100
Lip Enhancement 1ml £200
Facial Fillers £200 per 1ml
Volumiq £450 per session (2 vials - must be bought as a course)
Non Surgical Face Lift (Thread Lift) £600 per area
Skin Press Full Face £250
Skin Press Small Per Small Area £100
Cryo Therapy £60
Chemical Peel Light Peel and Microdermabrasion £85
Chemical Peel Deep Peel £150
Consultation £30 redeemable against service
Relaxon Top Up Relaxon £50 (must be within 2 weeks of 1st treatment)
Filler Top Up £100 (must be within 2 weeks of 1st appointment)

Open Hours
Updates

Company Name: HVM Address: 482 Pellbrook Road, 6 Warnford High Street, KT4 3JQ Phone: 0208 947 2186 Website: www.hollyvanmereaesthetics.co.uk

Please add more colour

Needs to be much cleaner and simpler Front page to include logo and price list Back page to inculde open hours and contact information including google map. Please no images with needles. Images of lips and faces are good, but try not to crowd copy on the pagei. No copy on top of images. White, grey, black and reds are good on colouring.

Target Market(s)

young market ages 22-45 years old mainly female
modern

Industry/Entity Type

Clinic

Number of Pages Required

4 page

Requirements
Must have
• Logo - logo must be in colour grey/silver
• Address (small map?)
• Phone number
• Web address
• Services
• Open hours
• Prices
• Images

```html
<!DOCTYPE html>
<html lang="en">
<head>
<meta charset="utf-8">
<title>HVM Price List &amp; Treatment</title>
<link rel="stylesheet" href="https://fonts.googleapis.com/css2?family=Cinzel:wght@400;600;700&family=Playfair+Display:wght@400&family=Montserrat:wght@700;800&family=Crimson+Pro:wght@400;500&display=swap">
<style>
:root{
  --red:#d3222a;
  --black:#0a0a0a;
  --grey:#a7a8aa;
  --grey-light:#d4d5d6;
  --grey-mid:#8d8e90;
  --grey-dark:#4a4a4b;
  --salmon:#e9967a;
  --white:#ffffff;
  --page:#e9e9ea;
}
*{box-sizing:border-box;margin:0;padding:0}
html,body{width:1200px;height:858px;overflow:hidden;background:var(--page)}
body{position:relative;font-family:"Crimson Pro",serif}

/* ---------- front cover ---------- */
.cover{position:absolute;left:30px;top:38px;width:552px;height:782px;background:var(--white);box-shadow:0 2px 10px rgba(0,0,0,.18);overflow:hidden}
.cover-band{position:absolute;left:0;top:0;width:100%;height:350px;background:var(--black)}
.cover-logo{position:absolute;top:70px;left:0;width:100%;text-align:center;font-family:"Cinzel",serif;font-size:76px;font-weight:400;color:var(--grey);letter-spacing:6px}
.cover-name{position:absolute;top:240px;left:0;width:100%;text-align:center;font-family:"Cinzel",serif;color:var(--grey);line-height:1}
.cover-name .line1{display:block;font-size:42px;letter-spacing:3px}
.cover-name .line2{display:block;font-size:62px;letter-spacing:5px;margin-top:2px}
.cover-tagline{position:absolute;left:58px;top:382px;width:186px;height:222px;border:1px dotted var(--grey-mid);outline:1px solid #ddd;outline-offset:-5px;display:flex;align-items:center;justify-content:center;text-align:center;font-family:"Playfair Display",serif;font-size:30px;line-height:1.33;color:var(--grey-mid);letter-spacing:-1.5px;transform:scaleX(.82)}
.cover-title{position:absolute;left:64px;top:620px;width:190px;height:158px;background:var(--red);border:3px solid var(--red);outline:1px solid var(--white);outline-offset:-7px;color:var(--white);font-family:"Cinzel",serif;text-align:center;padding-top:24px;line-height:1.05}
.cover-title .big{display:block;font-size:29px;font-weight:600;letter-spacing:2px}
.cover-title .amp{display:block;font-size:20px;margin:2px 0}
.cover-title .small{display:block;font-size:22px;letter-spacing:1px}
.cover-photo{position:absolute;left:262px;top:350px;width:290px;height:432px;background:radial-gradient(ellipse at 55% 55%,#e9c3ae 0%,#dcae97 45%,#f2f2f2 78%,#ffffff 100%)}

/* ---------- price sheet ---------- */
.sheet{position:absolute;left:618px;top:38px;width:552px;height:782px;background:var(--red);box-shadow:0 2px 10px rgba(0,0,0,.18);overflow:hidden}
.sheet-header{position:absolute;left:44px;top:16px;width:480px;height:128px;background:var(--grey-light);border-radius:0 8px 0 0;border-bottom:10px solid var(--black)}
.sheet-logo{position:absolute;left:36px;top:22px;font-family:"Cinzel",serif;font-size:28px;color:var(--black);letter-spacing:3px}
.sheet-name{position:absolute;left:10px;top:68px;font-family:"Cinzel",serif;color:var(--black);line-height:.95}
.sheet-name .line1{display:block;font-size:17px;letter-spacing:1.5px}
.sheet-name .line2{display:block;font-size:25px;letter-spacing:2px}
.sheet-label{position:absolute;right:-6px;top:36px;width:250px;height:70px;background:var(--black);color:var(--white);font-family:"Cinzel",serif;font-weight:700;font-size:26px;line-height:1.05;letter-spacing:2px;text-align:center;padding-top:6px}

.price-table{position:absolute;left:44px;top:162px;width:480px;border-collapse:collapse;table-layout:fixed}
.price-table th{background:var(--grey);color:var(--white);font-family:"Montserrat",sans-serif;font-weight:800;font-size:9px;letter-spacing:.5px;height:18px;border:1px solid var(--white)}
.price-table td{height:22px;border:1px solid var(--white);text-align:center;vertical-align:middle}
.price-table .tall td{height:42px}
.col-treat{width:228px}.col-desc{width:188px}.col-price{width:64px}
.treat{font-family:"Cinzel",serif;font-weight:600;font-size:14px;letter-spacing:1.5px;color:var(--white);line-height:1.05}
.treat.is-red{background:var(--red)}
.treat.is-black{background:var(--black)}
.desc{background:var(--grey-light);font-size:11px;font-weight:500;color:var(--black);line-height:1.15}
.price{background:var(--red);color:var(--white);font-size:16px;font-weight:500;line-height:1}
.price small{display:block;font-size:10px}

.consult{position:absolute;left:40px;top:510px;width:484px;height:26px;background:var(--salmon);color:var(--black);font-family:"Cinzel",serif;font-weight:600;font-size:14px;letter-spacing:1.5px;display:flex;align-items:center;padding-left:14px}
.consult .fee{color:var(--white);margin:0 6px;font-weight:400}
.topup{position:absolute;left:40px;width:484px;height:38px;display:flex}
.topup-one{top:540px}.topup-two{top:582px}
.topup-name{width:226px;display:flex;align-items:center;justify-content:center;color:var(--white);font-family:"Cinzel",serif;font-size:11px;letter-spacing:1.5px}
.topup-name b{font-size:16px;font-weight:600;margin-left:4px;letter-spacing:1px}
.topup-one .topup-name{background:var(--grey-mid)}
.topup-two .topup-name{background:var(--grey-dark)}
.topup-note{flex:1;margin-left:4px;background:var(--black);color:var(--white);font-size:11px;display:flex;align-items:center;justify-content:center}

.sheet-footer{position:absolute;left:0;top:628px;width:100%;height:154px;background:var(--grey-light);border-top:6px solid var(--black)}
.address{position:absolute;left:40px;top:10px;font-size:11px;line-height:1.2;color:var(--black);width:150px}
.address h3{font-size:11.5px;font-weight:500;margin-bottom:6px}
.call{position:absolute;left:32px;top:74px;width:160px;height:44px;background:var(--black);color:var(--white);border-radius:12px;text-align:center;padding-top:3px}
.call .phone{display:block;font-size:17px;font-weight:500;letter-spacing:.5px}
.call .web{display:block;font-size:8.5px;margin-top:1px}
.email{position:absolute;left:38px;top:124px;font-size:9.5px;color:var(--black)}
.map{position:absolute;left:198px;top:16px;width:164px;height:126px;border:2px solid var(--grey-dark);border-radius:10px;background:linear-gradient(135deg,#ece9e2,#dcdad3)}
.hours{position:absolute;left:372px;top:8px;width:170px;font-size:10.5px;color:var(--black);line-height:1.3}
.hours h3{font-family:"Montserrat",sans-serif;font-weight:700;font-size:11px;margin-bottom:2px}
.hours .row{display:flex}
.hours .day{width:74px}
.hours .note{font-size:9px;color:#666;text-align:center;padding-left:8px}
</style>
</head>
<body>

<section class="cover" aria-label="Front cover">
  <div class="cover-band"></div>
  <div class="cover-logo">HVM</div>
  <h1 class="cover-name"><span class="line1">HOLLY VANMERE</span><span class="line2">AESTHETICS</span></h1>
  <p class="cover-tagline">ACHIEVE<br>A FRESH<br>AND<br>BEAUTIFUL<br>YOU.</p>
  <div class="cover-title"><span class="big">PRICE</span><span class="big">LIST</span><span class="amp">&amp;</span><span class="small">TREATMENT</span></div>
  <div class="cover-photo" role="img" aria-label="Photo of a relaxed woman with closed eyes wearing a white towel on her head"></div>
</section>

<section class="sheet" aria-label="Price list">
  <header class="sheet-header">
    <div class="sheet-logo">HVM</div>
    <div class="sheet-name"><span class="line1">HOLLY VANMERE</span><span class="line2">AESTHETICS</span></div>
    <h2 class="sheet-label">PRICE LIST/<br>TREATMENT</h2>
  </header>

  <table class="price-table">
    <colgroup><col class="col-treat"><col class="col-desc"><col class="col-price"></colgroup>
    <thead><tr><th>TREATMENT</th><th>DESCRIPTION</th><th>PRICE</th></tr></thead>
    <tbody>
      <tr><td class="treat is-red">RELAXON</td><td class="desc">1 area</td><td class="price">£ 100</td></tr>
      <tr><td class="treat is-red">RELAXON</td><td class="desc">2 areas</td><td class="price">£ 150</td></tr>
      <tr><td class="treat is-red">RELAXON</td><td class="desc">3 areas</td><td class="price">£ 200</td></tr>
      <tr><td class="treat is-black">LIP ENHANCEMENT</td><td class="desc">0.5ml</td><td class="price">£ 100</td></tr>
      <tr><td class="treat is-black">LIP ENHANCEMENT</td><td class="desc">1ml</td><td class="price">£ 200</td></tr>
      <tr><td class="treat is-red">FACIAL FILLERS</td><td class="desc">1ml</td><td class="price">£ 200</td></tr>
      <tr class="tall"><td class="treat is-black">VOLUMIQ</td><td class="desc">(2 vials<br>must be bought as a course)</td><td class="price">£ 450<small>per session</small></td></tr>
      <tr class="tall"><td class="treat is-red">NON SURGICAL<br>FACE LIFT</td><td class="desc">(Thread Lift)</td><td class="price">£ 600<small>per area</small></td></tr>
      <tr><td class="treat is-black">SKIN PRESS</td><td class="desc">Full Face</td><td class="price">£ 250</td></tr>
      <tr><td class="treat is-black">SKIN PRESS</td><td class="desc">Small Per Small Area</td><td class="price">£ 100</td></tr>
      <tr><td class="treat is-red">CRYO THERAPY</td><td class="desc"></td><td class="price">£ 60</td></tr>
      <tr><td class="treat is-black">CHEMICAL PEEL</td><td class="desc">Light Peel and Microdermabrasion</td><td class="price">£ 85</td></tr>
      <tr><td class="treat is-black">CHEMICAL PEEL</td><td class="desc">Deep Peel</td><td class="price">£ 150</td></tr>
    </tbody>
  </table>

  <div class="consult">CONSULTATION <span class="fee">£30 REDEEMABLE</span> AGAINST SERVICE</div>
  <div class="topup topup-one"><div class="topup-name">RELAXON TOP UP: <b>RELAXON £50</b></div><div class="topup-note">(must be within 2 weeks of 1st treatment)</div></div>
  <div class="topup topup-two"><div class="topup-name">FILLER TOP UP: <b>£100</b></div><div class="topup-note">(must be within 2 weeks of 1st appointment)</div></div>

  <footer class="sheet-footer">
    <div class="address"><h3>HVM Address:</h3>482 Pellbrook Road,<br>6 Warnford High Street,<br>KT4 3JQ</div>
    <div class="call"><span class="phone">CALL 0208 947 2186</span><span class="web">www.hollyvanmereaesthetics.co.uk</span></div>
    <div class="email">hvmwarnfordbookings@hvmclinic.co.uk</div>
    <div class="map" role="img" aria-label="Street map showing the clinic location on Warnford High Street"></div>
    <div class="hours">
      <h3>Opening Times</h3>
      <div class="row"><span class="day">Monday</span><b>10am - 4pm</b></div>
      <div class="row"><span class="day">Tuesday</span><b>10am - 4pm</b></div>
      <div class="row"><span class="day">Wednesday</span><b>12pm - 8pm</b></div>
      <div class="row"><span class="day">Thursday</span><b>7:30am - 4:30pm</b></div>
      <div class="note">(at number 1 Ashcombe Street only)</div>
      <div class="row"><span class="day">Friday</span><b>10am - 2pm</b></div>
      <div class="row"><span class="day">Saturday</span><b>9am - 2pm</b></div>
      <div class="row"><span class="day">Sunday</span><b>Closed</b></div>
    </div>
  </footer>
</section>

</body>
</html>
```